MossVane Spa, Skincare and Cosmetics website

I need a website for MossVane (putting the glow back into people's skin) which allows viewers to access information about Beauty Spa packaging and facilities as well as online skincare and cosmetic products. Our distinctive difference is that our products are certified organic. We want to target a luxury high income niche market (age 30-50). I want all colours to be "baby colours" preferably background to be "baby metallic pink" (but please don't make the website too immature) with curves as patterns. I want a romantic vintage look.

The website needs to look:
1. elegant (prestige and luxury)
2. bright (baby colours mainly)
3. European curves and signature patterns
4. Can include Pearl related pics (but not a must)

The website pages needs to have:
1. pages ordering skincare/cosmetics
2. shopping cart and payment
3. about us and about our product differences
4. contact us
5. booking for spa treatments and packages

I have attached our logo and also packaging label styles.

Industry/Entity Type

Cosmetics

```html
<!DOCTYPE html>
<html lang="en">
<head>
<meta charset="utf-8">
<title>MossVane Spa, Skincare and Cosmetics</title>
<link rel="stylesheet" href="https://fonts.googleapis.com/css2?family=Raleway:ital,wght@0,300;0,400;0,500;1,300&family=Roboto+Condensed:wght@400;700&family=Open+Sans:wght@400;600;700&display=swap">
<style>
:root{
  --pink:#ee8fa3;
  --pink-deep:#d81e62;
  --pink-hero:#e0467d;
  --pink-soft:#f4a7b5;
  --peach:#f3b98f;
  --peach-light:#fde0c4;
  --cream:#f2e7b2;
  --text:#5a4a45;
  --text-soft:#7d6f6a;
  --brown:#9a5b4e;
  --white:#ffffff;
  --grey:#e9e6e3;
}
*{box-sizing:border-box;margin:0;padding:0}
html,body{width:1200px;height:2410px;overflow:hidden}
body{
  position:relative;
  font-family:"Open Sans",Arial,sans-serif;
  color:var(--text);
  background:linear-gradient(180deg,#f6c8b1 0%,#f5d2b2 14%,#f3dfb4 28%,#f1e5b4 50%,#efe3ad 100%);
}
.abs{position:absolute}

/* header */
.brand{left:104px;top:40px;display:flex;align-items:center;gap:12px;
  font-family:"Raleway",sans-serif;font-weight:500;font-size:34px;color:var(--pink-deep)}
.brand-mark{width:18px;height:18px;background:var(--pink)}
.brand-tag{left:134px;top:92px;font-family:"Raleway",sans-serif;font-size:12px;color:var(--pink-deep);letter-spacing:1px}
.flowers-top{left:320px;top:16px;width:550px;height:160px;border-radius:50% 50% 40% 40%;
  background:radial-gradient(ellipse at 55% 45%,#c2358e 0%,#d98dc6 40%,rgba(246,235,240,.8) 70%,rgba(246,200,177,0) 75%)}
.call{left:848px;top:48px;font-family:"Raleway",sans-serif;font-style:italic;font-weight:300;font-size:20px;color:var(--white)}
.phone{left:888px;top:72px;font-family:"Raleway",sans-serif;font-style:italic;font-weight:300;font-size:29px;color:var(--white);letter-spacing:1px}

/* hero frame */
.frame{left:108px;top:153px;width:999px;height:626px;border-radius:30px;
  background:linear-gradient(180deg,#fafafa,#e4e4e4);box-shadow:0 10px 18px rgba(120,80,60,.25)}
.slide{left:124px;top:233px;width:968px;height:498px;border-radius:0 0 18px 18px;overflow:hidden;
  background:linear-gradient(90deg,#ffffff 0%,#fdf9f7 45%,#f6e7df 60%)}
.hero-photo{position:absolute;right:0;top:0;width:470px;height:498px;
  background:radial-gradient(ellipse at 65% 50%,#b58465 0%,#d5b09a 35%,rgba(240,222,212,.6) 65%,rgba(253,249,247,0) 80%)}
.hero-title{left:193px;top:372px;font-family:"Raleway",sans-serif;font-weight:300;font-size:51px;line-height:1.0;color:var(--pink-hero)}
.hero-sub{left:193px;top:424px;font-family:"Raleway",sans-serif;font-weight:300;font-size:51px;line-height:1.0;color:#777}
.hero-copy{left:193px;top:498px;font-family:"Raleway",sans-serif;font-size:17px;line-height:26px;color:var(--brown);letter-spacing:.5px}
.btn-more{left:193px;top:580px;width:128px;height:40px;border-radius:20px;
  background:linear-gradient(180deg,#f4cfb7,#d99a82);color:var(--white);
  font-family:"Raleway",sans-serif;font-size:19px;display:flex;align-items:center;padding-left:20px;gap:10px}
.dots{left:544px;top:759px;display:flex;gap:10px}
.dots span{width:17px;height:17px;border-radius:50%;background:#dcdcdc;box-shadow:inset 0 1px 2px rgba(0,0,0,.2)}
.dots .on{background:#b73a6a}
.decor{left:0;top:700px;width:680px;height:190px;
  background:radial-gradient(ellipse at 50% 60%,rgba(255,255,255,.9) 0%,rgba(230,220,180,.7) 30%,rgba(205,120,170,.4) 55%,rgba(240,230,180,0) 72%)}

/* hero footer */
.divider-v{left:702px;top:822px;width:1px;height:61px;background:var(--white)}
.volume{left:731px;top:832px;font-size:12px;color:var(--white)}
.slider{left:811px;top:838px;width:96px;height:4px;background:var(--white)}
.slider-fill{left:811px;top:838px;width:76px;height:4px;background:#d76a8a}
.slider-plus{left:905px;top:830px;font-size:13px;color:#d76a8a}
.copy-top{left:731px;top:863px;font-size:11px;color:var(--white)}
.copy-top a{color:var(--white);margin-left:22px;padding-left:18px;border-left:1px solid var(--white)}
.social{top:824px;width:27px;height:27px;border-radius:50%}

/* about */
.about-title{left:183px;top:940px;font-family:"Raleway",sans-serif;font-weight:300;font-size:43px;color:var(--pink-hero)}
.about-lead{left:185px;top:1002px;font-size:11.5px;font-weight:600;color:#8b2f4e}
.about-text{left:185px;top:1022px;width:895px;font-size:11.5px;line-height:17.5px;color:var(--text-soft)}

/* products */
.products-title{left:183px;top:1108px;font-family:"Raleway",sans-serif;font-weight:300;font-size:31px;color:#e1916a}
.arrow{top:1132px;width:24px;height:23px;background:#8e2a62;display:flex;align-items:center;justify-content:center}
.card{top:1163px;width:210px;height:233px;background:var(--white);box-shadow:0 0 4px rgba(0,0,0,.15)}
.card-photo{position:absolute;left:34px;top:14px;width:142px;height:120px;
  background:radial-gradient(ellipse at 50% 50%,#b97ca0 0%,#e1d3dc 35%,#f6f2f4 62%,#ffffff 75%)}
.card-name{position:absolute;top:152px;width:100%;text-align:center;font-size:12px;color:var(--text-soft)}
.card-price{position:absolute;top:170px;width:100%;text-align:center;font-size:12px;color:var(--pink-deep)}
.card-info{position:absolute;left:4px;top:205px;width:101px;height:18px;background:var(--grey);font-size:10px;color:#999;padding-left:20px;line-height:18px}
.card-cart{position:absolute;left:105px;top:205px;width:101px;height:18px;background:var(--pink-deep);font-size:11px;color:var(--white);text-align:center;line-height:18px}
.sep{top:1185px;width:6px;height:180px;background:linear-gradient(90deg,rgba(190,170,140,.3),#ffffff,rgba(190,170,140,.3));border-radius:3px}

/* treatments */
.tabs-panel{left:198px;top:1426px;width:498px;height:884px;background:var(--white);border-radius:6px;box-shadow:0 0 5px rgba(0,0,0,.12)}
.tab-bar{left:198px;top:1426px;width:498px;height:50px;background:var(--pink-soft);border-radius:6px 6px 0 0}
.tab{top:1436px;font-family:"Roboto Condensed",sans-serif;font-size:21px;color:#7b4a52}
.tab.active{color:var(--white)}
.tr-name{left:209px;font-family:"Roboto Condensed",sans-serif;font-weight:700;font-size:21px;color:#555}
.tr-photo{left:209px;width:233px;height:154px}
.tr-text{left:458px;width:222px;font-size:12px;line-height:17px;text-align:justify;color:var(--text-soft)}
.tr-price{left:458px;font-family:"Roboto Condensed",sans-serif;font-weight:700;font-size:19px;color:var(--pink)}
.tr-rule{left:209px;width:475px;height:1px;background:#dcdcdc}
.btn-all{left:477px;top:2250px;width:206px;height:31px;border-radius:4px;background:var(--pink);
  font-family:"Roboto Condensed",sans-serif;font-weight:700;font-size:18px;color:var(--white);text-align:center;line-height:31px}

/* side panels */
.panel{left:715px;width:372px;background:var(--white);border-radius:6px;box-shadow:0 0 5px rgba(0,0,0,.12)}
.panel-head{left:715px;width:372px;height:35px;background:var(--pink-soft);border-radius:6px 6px 0 0;
  font-size:13px;font-weight:600;color:var(--white);padding-left:20px;line-height:35px;letter-spacing:.5px}
.no-products{left:734px;top:1475px;font-size:12px;color:var(--pink-soft);letter-spacing:.5px}
.dotted{left:734px;width:199px;border-top:1px dashed #999}
.cart-bar{left:734px;width:194px;height:24px;background:var(--pink-soft);display:flex;justify-content:space-between;
  padding:0 24px 0 10px;font-size:11px;color:var(--white);line-height:24px}
.cart-bar b{color:#4a3a3a;font-weight:600}
.btn-cart{left:736px;top:1650px;width:67px;height:24px;background:var(--grey);font-size:13px;color:#555;text-align:center;line-height:24px}
.btn-checkout{left:816px;top:1650px;width:112px;height:24px;background:var(--pink-deep);font-size:13px;color:var(--white);text-align:center;line-height:24px}
.spa-name{left:715px;top:1758px;width:372px;text-align:center;font-size:12px;color:var(--text-soft)}
.spa-price{left:715px;top:1778px;width:372px;text-align:center;font-size:12px;color:var(--pink-deep)}
.spa-photo{left:771px;top:1796px;width:250px;height:250px;border-radius:50%;border:4px solid #f6ece4;
  background:radial-gradient(circle at 62% 45%,#c9318a 0%,#e48cbb 22%,#f1dbe0 45%,#ede8e0 70%,#e4ddd2 100%)}
.spa-text{left:735px;top:2146px;width:332px;text-align:center;font-size:13px;line-height:20px;color:#b0566a}
.btn-read{left:829px;top:2247px;width:138px;height:42px;border-radius:4px;background:linear-gradient(180deg,#fde0b8,#f4b57f);
  font-size:12px;color:#7a4a3a;text-align:center;line-height:42px}

/* footer */
.pay{top:2343px;width:46px;height:23px;border-radius:3px;background:#dedcd6;border:1px solid #bdb9b0}
.foot-links{right:101px;top:2353px;font-size:11px;color:#555}
.foot-links span{margin:0 8px;color:#777}
.foot-copy{right:101px;top:2372px;font-size:11px;color:#555}
</style>
</head>
<body>

<!-- header -->
<div class="abs brand"><span class="brand-mark"></span>MossVane</div>
<div class="abs brand-tag">your sample text</div>
<div class="abs flowers-top" role="img" aria-label="Pink and white orchid sprays across the top of the frame"></div>
<div class="abs call">Call to shedule</div>
<div class="abs phone">1-800-555-0142</div>

<svg class="abs" style="left:22px;top:168px" width="1156" height="70" viewBox="0 0 1156 70" aria-hidden="true">
  <defs>
    <linearGradient id="ribbon" x1="0" y1="0" x2="0" y2="1">
      <stop offset="0" stop-color="#f7a3bd"/><stop offset="1" stop-color="#e46f92"/>
    </linearGradient>
  </defs>
  <path d="M0 18 L100 8 L100 58 L0 52 L30 35 Z" fill="#e37d9b"/>
  <path d="M1156 18 L1056 8 L1056 58 L1156 52 L1126 35 Z" fill="#e37d9b"/>
  <rect x="80" y="5" width="996" height="58" rx="4" fill="url(#ribbon)"/>
  <g fill="#b8395f">
    <circle cx="222" cy="34" r="4"/><circle cx="343" cy="34" r="4"/><circle cx="472" cy="34" r="4"/>
    <circle cx="655" cy="34" r="4"/><circle cx="770" cy="34" r="4"/><circle cx="903" cy="34" r="4"/>
  </g>
  <g font-family="Raleway, sans-serif" font-size="19" fill="#ffffff">
    <text x="145" y="41" fill="#fde3e8">HOME</text>
    <text x="251" y="41">ABOUT</text>
    <text x="365" y="41">SERVICES</text>
    <text x="503" y="41">CONSULTANT</text>
    <text x="678" y="41">PRICES</text>
    <text x="792" y="41">GALLERY</text>
    <text x="926" y="41">CONTACTS</text>
  </g>
</svg>

<!-- hero -->
<div class="abs frame"></div>
<svg class="abs" style="left:22px;top:168px" width="1156" height="70" viewBox="0 0 1156 70" aria-hidden="true">
  <rect x="80" y="5" width="996" height="58" rx="4" fill="#f08aa9"/>
  <g fill="#b8395f">
    <circle cx="222" cy="34" r="4"/><circle cx="343" cy="34" r="4"/><circle cx="472" cy="34" r="4"/>
    <circle cx="655" cy="34" r="4"/><circle cx="770" cy="34" r="4"/><circle cx="903" cy="34" r="4"/>
  </g>
  <g font-family="Raleway, sans-serif" font-size="19" fill="#ffffff">
    <text x="145" y="41" fill="#fde3e8">HOME</text>
    <text x="251" y="41">ABOUT</text>
    <text x="365" y="41">SERVICES</text>
    <text x="503" y="41">CONSULTANT</text>
    <text x="678" y="41">PRICES</text>
    <text x="792" y="41">GALLERY</text>
    <text x="926" y="41">CONTACTS</text>
  </g>
</svg>
<div class="abs slide">
  <div class="hero-photo" role="img" aria-label="Woman with long straight auburn hair seen in profile"></div>
</div>
<div class="abs hero-title">Beauty Expert Spa</div>
<div class="abs hero-sub">Moss Vane</div>
<div class="abs hero-copy">LOREM IPSUM DOLOR SIT AMET CONSE CTETUR<br>ADIPISICING ELIT, SED DO EIUSMOD.</div>
<div class="abs btn-more">MORE
  <svg width="14" height="14" viewBox="0 0 14 14" aria-hidden="true"><path d="M2 1 L13 7 L2 13 L5 7 Z" fill="#ffffff"/></svg>
</div>
<div class="abs dots"><span></span><span></span><span class="on"></span><span></span><span></span></div>
<div class="abs decor" role="img" aria-label="Spa still life of orchids, rolled towels, oil bottle, candles, stones and daisies"></div>

<div class="abs divider-v"></div>
<div class="abs volume">Volume:</div>
<div class="abs slider"></div>
<div class="abs slider-fill"></div>
<div class="abs slider-plus">+</div>
<div class="abs copy-top">© 2013. MOSSVANE <a>Privacy policy</a></div>
<div class="abs social" style="left:985px;background:#8a8fa6"></div>
<div class="abs social" style="left:1020px;background:#8fb0c4"></div>
<div class="abs social" style="left:1057px;background:#86bcd9"></div>

<!-- about -->
<div class="abs about-title">About Us!</div>
<div class="abs about-lead">Contrary to popular belief, Lorem Ipsum is not simply random text.</div>
<div class="abs about-text">Lorem ipsum dolor sit amet, consectetuer adipiscing elit. Nam nibh. Nunc varius facilisis eros. Sed erat. In in velit quis arcu ornare laoreet. Curabitur adipiscing luctus massa. Integer ut purus ac augue commodo commodo. Nunc nec mi eu justo tempor consectetuer. Etiam vitae nisl. In dignissim lacus ut ante. Cras elit lectus, bibendum a, adipiscing vitae,</div>

<!-- products -->
<div class="abs products-title">Our Latest Products</div>
<div class="abs arrow" style="left:1007px">
  <svg width="10" height="12" viewBox="0 0 10 12" aria-hidden="true"><path d="M8 1 L2 6 L8 11" stroke="#fff" stroke-width="2" fill="none"/></svg>
</div>
<div class="abs arrow" style="left:1036px">
  <svg width="10" height="12" viewBox="0 0 10 12" aria-hidden="true"><path d="M2 1 L8 6 L2 11" stroke="#fff" stroke-width="2" fill="none"/></svg>
</div>

<div class="abs card" style="left:183px">
  <div class="card-photo" role="img" aria-label="Pair of square silver cufflinks with pink stones"></div>
  <div class="card-name">Lorem ipsum dolor sit amet</div>
  <div class="card-price">Our Price : AUD $32</div>
  <div class="card-info">MORE INFO</div><div class="card-cart">ADD TO CART</div>
</div>
<div class="abs sep" style="left:466px"></div>
<div class="abs card" style="left:540px">
  <div class="card-photo" role="img" aria-label="Pair of square silver cufflinks with pink stones"></div>
  <div class="card-name">Lorem ipsum dolor sit amet</div>
  <div class="card-price">Our Price : AUD $32</div>
  <div class="card-info">MORE INFO</div><div class="card-cart">ADD TO CART</div>
</div>
<div class="abs sep" style="left:806px"></div>
<div class="abs card" style="left:882px">
  <div class="card-photo" role="img" aria-label="Pair of square silver cufflinks with pink stones"></div>
  <div class="card-name">Lorem ipsum dolor sit amet</div>
  <div class="card-price">Our Price : AUD $32</div>
  <div class="card-info">MORE INFO</div><div class="card-cart">ADD TO CART</div>
</div>

<!-- treatments -->
<div class="abs tabs-panel"></div>
<div class="abs tab-bar"></div>
<div class="abs tab active" style="left:243px">Treatments</div>
<div class="abs tab" style="left:389px">Packages</div>
<div class="abs tab" style="left:522px">Special Events</div>

<div class="abs tr-name" style="top:1530px">Deep Tissue Massage</div>
<div class="abs tr-photo" style="top:1571px;background:linear-gradient(135deg,#3a2a24,#b07a5e 45%,#e6b49a 70%,#c8324e)" role="img" aria-label="Therapist giving a back massage"></div>
<div class="abs tr-text" style="top:1572px">This intense releases stimulates the blood flow all over the body and relieves knotted muscles. Best for those with muscle tightness or tension.</div>
<div class="abs tr-price" style="top:1673px">60 min $70</div>
<div class="abs tr-rule" style="top:1746px"></div>

<div class="abs tr-name" style="top:1770px">Facial</div>
<div class="abs tr-photo" style="top:1812px;background:linear-gradient(135deg,#f1ece4,#e8c9b4 50%,#a8c46a 75%,#f4f0ea)" role="img" aria-label="Client relaxing with a face mask and cucumber slices"></div>
<div class="abs tr-text" style="top:1813px">A seaweed wrap plus a cool soothing contour mask is applied to the face. Helps skin moisturize, tone, and diffuse redness, thus restoring your epidermis to a healthy glow.</div>
<div class="abs tr-price" style="top:1913px">60 min $70</div>
<div class="abs tr-rule" style="top:1980px"></div>

<div class="abs tr-name" style="top:2003px">Nails</div>
<div class="abs tr-photo" style="top:2043px;background:linear-gradient(135deg,#e9d2b0,#d9a98a 45%,#f0e3b0 75%,#e4d4b4)" role="img" aria-label="Hands resting beside bottles of oil for a manicure"></div>
<div class="abs tr-text" style="top:2044px">Our signature treatment begins with a calming foot soak in rosewater with petals. It is then followed by nail shaping of square of oval.</div>
<div class="abs tr-price" style="top:2128px">60 min $70</div>
<div class="abs tr-rule" style="top:2218px"></div>
<div class="abs btn-all">See All Our Treatments</div>

<!-- cart -->
<div class="abs panel" style="top:1428px;height:263px"></div>
<div class="abs panel-head" style="top:1428px">CART ▴</div>
<div class="abs no-products">NO PRODUCTS</div>
<div class="abs dotted" style="top:1505px"></div>
<div class="abs cart-bar" style="top:1526px">SHIPPING<b>$0.00</b></div>
<div class="abs dotted" style="top:1565px"></div>
<div class="abs cart-bar" style="top:1580px">TOTAL<b>$0.00</b></div>
<div class="abs dotted" style="top:1618px"></div>
<div class="abs btn-cart">CART</div>
<div class="abs btn-checkout">CHECK OUT</div>

<!-- selection of spa -->
<div class="abs panel" style="top:1711px;height:597px"></div>
<div class="abs panel-head" style="top:1711px">SELECTION OF SPA</div>
<div class="abs spa-name">Lorem ipsum dolor sit amet</div>
<div class="abs spa-price">Our Price : AUD $32</div>
<div class="abs spa-photo" role="img" aria-label="Pink gerbera daisies floating in a glass bowl"></div>
<div class="abs spa-text">Lorem ipsum dolor sit amet adipiscing elit, sed diam nonummy nibh euismod tincidunt ut. Lorem ipsum dolor sit amet adipiscing elit, sed diam nonummy nibh euismod tincidunt ut.</div>
<div class="abs btn-read">READ MORE</div>

<!-- footer -->
<div class="abs pay" style="left:206px"></div>
<div class="abs pay" style="left:271px;width:36px"></div>
<div class="abs pay" style="left:316px;width:36px"></div>
<div class="abs foot-links">Specials<span>|</span>New products<span>|</span>Top sellers<span>|</span>Our stores<span>|</span>Contact us<span>|</span>Terms and conditions of use<span>|</span>About us</div>
<div class="abs foot-copy">©2014 Powered by Lumenweave™. All rights reserved</div>

</body>
</html>
```